design an extra page for our profile

we are looking for someone to create another page like the attached but with the below changes:
heading changed to (Construction)
icons changed and names to reflect new services i.e
- Residential Building
- Commercial Building
- Landscaping
- Concrete
- Painting

the very bottom of the page is to stay the same with our office info

```html
<!DOCTYPE html>
<html lang="en">
<head>
<meta charset="utf-8">
<title>Construction Services</title>
<link rel="stylesheet" href="https://fonts.googleapis.com/css2?family=Nunito+Sans:wght@300;400;600;700;800&display=swap">
<style>
  :root {
    --blue: #1f3ee3;
    --red: #ee3a1c;
    --rust: #b8452d;
    --white: #ffffff;
    --sun: #f0461f;
    --sand: #f2b23a;
  }
  * { box-sizing: border-box; margin: 0; padding: 0; }
  html, body { width: 926px; height: 1200px; overflow: hidden; background: var(--white); }
  body { font-family: "Nunito Sans", Arial, sans-serif; }
  .page { position: relative; width: 926px; height: 1200px; overflow: hidden; background: var(--white); }

  .masthead {
    position: absolute; left: 0; top: 0; width: 926px; height: 307px;
    background: var(--blue); color: var(--white); text-align: center;
  }
  .masthead__title {
    position: absolute; left: 0; right: 0; top: 50px;
    font-size: 44px; letter-spacing: 0.5px; line-height: 1;
  }
  .masthead__title strong { font-weight: 800; }
  .masthead__title span { font-weight: 300; }
  .masthead__rule {
    position: absolute; left: 82px; width: 762px; top: 124px;
    height: 1px; background: rgba(255,255,255,0.7);
  }
  .masthead__offer {
    position: absolute; left: 138px; right: 138px; top: 146px;
    font-size: 28px; line-height: 42px; font-weight: 400;
  }

  .service {
    position: absolute; display: flex; align-items: center; gap: 20px;
    color: var(--blue); font-size: 28px; font-weight: 600; line-height: 1.3;
  }
  .service__icon {
    width: 78px; height: 78px; border-radius: 50%;
    border: 2px solid var(--rust); flex: none;
    display: flex; align-items: center; justify-content: center;
  }
  .service__icon svg { width: 44px; height: 44px; }
  .service--residential { left: 71px; top: 373px; }
  .service--commercial  { left: 386px; top: 373px; }
  .service--landscaping { left: 71px; top: 494px; }
  .service--painting    { left: 71px; top: 612px; }
  .service--concrete    { left: 71px; top: 730px; }

  .band-red {
    position: absolute; left: 0; top: 917px; width: 926px; height: 22px; background: var(--red);
  }
  .band-blue {
    position: absolute; left: 0; top: 956px; width: 926px; height: 244px; background: var(--blue);
  }

  .scene { position: absolute; left: 360px; top: 480px; width: 566px; height: 580px; }

  .footer { position: absolute; left: 0; top: 1060px; width: 926px; height: 140px; color: var(--white); }
  .brand {
    position: absolute; left: 36px; top: 28px;
    display: flex; align-items: center; gap: 10px;
    font-size: 30px; font-weight: 800; color: var(--white); letter-spacing: 1px;
  }
  .brand__dot { width: 22px; height: 22px; border-radius: 50%; background: var(--white); }
  .footer__line {
    position: absolute; left: 207px;
    font-size: 20px; white-space: nowrap; line-height: 1;
  }
  .footer__line--office { top: 31px; }
  .footer__line--web { top: 81px; }
  .footer__line b { font-weight: 800; }
  .footer__rule {
    position: absolute; left: 207px; right: 33px; top: 66px; height: 1px; background: rgba(255,255,255,0.7);
  }
  .sep { display: inline-block; width: 1px; height: 20px; background: var(--white); vertical-align: -3px; margin: 0 5px; }
</style>
</head>
<body>
<main class="page">
  <header class="masthead">
    <h1 class="masthead__title"><strong>CONSTRUCTION</strong> <span>SERVICES</span></h1>
    <div class="masthead__rule"></div>
    <p class="masthead__offer">As new tenants to buiding and as a way of introducing ourselves we would like to offer a 10% discount on any of the below services.</p>
  </header>

  <div class="service service--residential">
    <div class="service__icon">
      <svg viewBox="0 0 44 44" fill="none" stroke="#b8452d" stroke-width="2">
        <rect x="8" y="8" width="28" height="30"/><line x1="6" y1="8" x2="38" y2="8"/>
        <rect x="12" y="13" width="5" height="5"/><rect x="27" y="13" width="5" height="5"/>
        <rect x="12" y="23" width="5" height="5"/><rect x="27" y="23" width="5" height="5"/>
        <rect x="19" y="28" width="6" height="10"/>
      </svg>
    </div>
    <span>Residential<br>Building</span>
  </div>

  <div class="service service--commercial">
    <div class="service__icon">
      <svg viewBox="0 0 44 44" fill="none" stroke="#b8452d" stroke-width="2">
        <line x1="18" y1="6" x2="18" y2="40"/><line x1="24" y1="6" x2="24" y2="40"/>
        <line x1="4" y1="10" x2="40" y2="10"/><line x1="18" y1="18" x2="24" y2="24"/>
        <line x1="24" y1="18" x2="18" y2="24"/><line x1="34" y1="10" x2="34" y2="22"/>
        <rect x="31" y="22" width="6" height="5"/><line x1="12" y1="40" x2="30" y2="40"/>
      </svg>
    </div>
    <span>Commercial<br>Building</span>
  </div>

  <div class="service service--landscaping">
    <div class="service__icon">
      <svg viewBox="0 0 44 44" fill="none" stroke="#b8452d" stroke-width="2">
        <rect x="6" y="28" width="32" height="6"/><rect x="10" y="22" width="24" height="6"/>
        <rect x="14" y="16" width="16" height="6"/><line x1="22" y1="28" x2="22" y2="34"/>
        <line x1="16" y1="22" x2="16" y2="28"/><line x1="28" y1="22" x2="28" y2="28"/>
      </svg>
    </div>
    <span>Landscaping</span>
  </div>

  <div class="service service--painting">
    <div class="service__icon">
      <svg viewBox="0 0 44 44" fill="none" stroke="#b8452d" stroke-width="2">
        <path d="M11 14 L14 38 H30 L33 14 Z"/><path d="M11 14 C11 4 33 4 33 14"/>
        <path d="M14 20 H30 V26 C26 24 22 30 18 26 L14 26"/>
      </svg>
    </div>
    <span>Painting</span>
  </div>

  <div class="service service--concrete">
    <div class="service__icon">
      <svg viewBox="0 0 44 44" fill="none" stroke="#b8452d" stroke-width="2">
        <path d="M8 16 H34 L30 28 H14 Z"/><line x1="4" y1="12" x2="10" y2="16"/>
        <circle cx="30" cy="34" r="4"/><line x1="26" y1="28" x2="30" y2="30"/>
        <path d="M14 16 C16 10 24 9 28 16"/>
      </svg>
    </div>
    <span>Concrete</span>
  </div>

  <div class="band-red"></div>
  <div class="band-blue"></div>

  <svg class="scene" viewBox="0 0 566 580" role="img" aria-label="Illustration of a multi-storey building under construction with a tower crane, excavator and a worker, set against an orange sun and city skyline">
    <defs>
      <clipPath id="sun-clip"><rect x="0" y="0" width="566" height="476"/></clipPath>
    </defs>
    <circle cx="260" cy="338" r="235" fill="#f0461f" clip-path="url(#sun-clip)"/>
    <ellipse cx="280" cy="540" rx="272" ry="24" fill="#f2b23a"/>
  </svg>

  <footer class="footer">
    <div class="brand"><span class="brand__dot"></span>ARVEN</div>
    <p class="footer__line footer__line--office"><b>HOME office:</b> 1300 48 2096 &nbsp; Suite 2.07, 14 Meridian Way Kellyville</p>
    <div class="footer__rule"></div>
    <p class="footer__line footer__line--web"><b>WWW.ARVEN-WORKS.com.AU</b> Sydney <span class="sep"></span>Canberra <span class="sep"></span>Brisbane <span class="sep"></span>Melbourne</p>
  </footer>
</main>
</body>
</html>
```